Web Design Project for Film Business

We need a web design for a new company based in Bondi Beach, Sydney, Australia. We basically provide filming and video editing services. Our targets are basically corporate videos, wedding videos and other types of functions.
The important thing to know about us is that we are not just people that press the record button, we consider ourselves story tellers. We can make something boring like a conference look interesting to watch and we can also make a wedding look like a blockbuster movie that you can't look away from until its finished.
We need something as new and fresh as Bondi Beach. A young place where people come from all over the world to enjoy summer and we are lucky to be based here.
To see some of our work please visit our tavlora Channel. Make sure you watch a couple of wedding video and the corporate video so you can have a better understanding about our style.
Please note- we are not trying to market ourselves exclusively as wedding videographers, nor do we want to exploit the idea of the beach.

http://tavlora.com/channels/815374

sites that we really like:

http://www.quillpathreels.co.uk/
http://www.marnowebb.co.uk/

Target Market(s)

Couples - Corporate

Industry/Entity Type

Business

Requirements
Must have
• 5 to 6 pages (we are still deciding)
-main page
-our story (story about Karrow Films)
-your story (page designated for wedding videos)
-your business (page designated for corporate videos)
-contact us
-other stuff
Nice to have
• I would like to see some animation. Maybe you can animate our logo. Up to the designer

```html
<!DOCTYPE html>
<html lang="en">
<head>
<meta charset="utf-8">
<title>Karrow Films — Your Story</title>
<link href="https://fonts.googleapis.com/css2?family=Arimo:wght@400;700&display=swap" rel="stylesheet">
<style>
  :root {
    --page-bg: #000000;
    --header-top: #6a6a6a;
    --header-bottom: #555555;
    --header-shadow: #1a1a1a;
    --text-light: #ffffff;
    --nav-muted: #8a8a8a;
    --accent: #7d6150;
    --badge-light: #eef1f6;
    --badge-border: #9aa6bf;
    --follow-blue: #3d8fc4;
    --photo-dark: #2a2622;
    --photo-mid: #5a5048;
  }
  * { margin: 0; padding: 0; box-sizing: border-box; }
  html, body {
    width: 1200px; height: 748px; overflow: hidden;
    background: var(--page-bg);
    font-family: "Arimo", Arial, sans-serif;
  }
  .site { position: relative; width: 1200px; height: 748px; }

  .site-header {
    position: absolute; left: 0; top: 0; width: 1200px; height: 151px;
    background: linear-gradient(90deg, var(--header-shadow) 0%, var(--header-bottom) 35%, var(--header-top) 60%, var(--header-bottom) 100%);
  }
  .header-scenery {
    position: absolute; left: 0; top: 0; width: 620px; height: 151px;
    background: linear-gradient(180deg, rgba(0,0,0,0) 40%, rgba(0,0,0,0.85) 100%);
  }
  .brand {
    position: absolute; left: 47px; top: 24px;
    font-weight: 700; font-size: 62px; line-height: 70px;
    letter-spacing: 2px; color: var(--text-light);
  }
  .social {
    position: absolute; top: 98px; height: 24px; display: flex; align-items: center;
    font-size: 13px; border-radius: 3px;
  }
  .social-like {
    left: 47px; width: 54px; background: var(--badge-light);
    border: 1px solid var(--badge-border); color: #333; padding-left: 5px; gap: 5px;
  }
  .social-count {
    left: 108px; width: 40px; background: #fff; border: 1px solid #bbb;
    color: #333; justify-content: center; font-size: 12px;
  }
  .social-follow {
    left: 159px; width: 91px; background: var(--follow-blue);
    color: #fff; padding-left: 6px; gap: 8px; font-weight: 700;
  }
  .social-square { width: 13px; height: 13px; background: currentColor; opacity: .6; }

  .main-nav {
    position: absolute; top: 96px; left: 0; height: 55px; width: 1200px;
  }
  .nav-item {
    position: absolute; top: 0; height: 55px; line-height: 52px;
    font-size: 15px; color: var(--nav-muted); text-decoration: none;
  }
  .nav-item.is-active {
    background: var(--page-bg); color: var(--text-light);
    padding: 0 15px; margin-left: -15px;
  }

  .feature-photo {
    position: absolute; left: 46px; top: 196px; width: 806px; height: 455px;
    background: linear-gradient(90deg, var(--photo-mid) 0%, var(--photo-dark) 55%, #141210 100%);
  }
  .feature-copy {
    position: absolute; left: 920px; top: 253px; width: 260px;
    font-size: 27px; line-height: 35px; color: var(--text-light);
  }
  .feature-copy p + p { margin-top: 35px; }
  .feature-copy .highlight { color: var(--accent); font-weight: 700; }
</style>
</head>
<body>
<div class="site">
  <header class="site-header">
    <div class="header-scenery" role="img" aria-label="Silhouette of palm trees against the header band"></div>
    <div class="brand">KARROW FILMS</div>
    <div class="social social-like"><span class="social-square"></span>Like</div>
    <div class="social social-count">238K</div>
    <div class="social social-follow"><span class="social-square"></span>Follow</div>
    <nav class="main-nav">
      <a class="nav-item" style="left:645px" href="#">our story</a>
      <a class="nav-item is-active" style="left:743px" href="#">your story</a>
      <a class="nav-item" style="left:849px" href="#">your business</a>
      <a class="nav-item" style="left:980px" href="#">contact us</a>
      <a class="nav-item" style="left:1084px" href="#">our films</a>
    </nav>
  </header>

  <div class="feature-photo" role="img" aria-label="Bride and groom holding hands beside tall carved wooden doors and a stone column"></div>

  <div class="feature-copy">
    <p>We are not<br>people that just<br>press the<br>record button.</p>
    <p>We get to<br>know you<br>and can<br><span class="highlight">tell your story</span><br>like no one else.</p>
  </div>
</div>
</body>
</html>
```